Web Site for Strategy and Technology Consulting Company

We are looking for a website design that engages potential customers to understand our services and contact us. In this contest, we are looking for a homepage design, but the winning designer will be favored for the design of some of the more complicated interior pages of the site. An additional contest (or contests) for these pages will be added soon.

PLATROM AND RESPONSIVE DESIGN
The site will be implemented in WordPress using the Elementor page builder.
We are looking for a design that will look good on phones are well as laptop browsers.

UPLOADED FILES INCLUDE:
1a A wireframe of the homepage we are looking for. The Uploaded PDF also includes a draft of the text proposed for the homepage. Designers are free to go beyond the wireframe, but all elements of the wireframe should be included.
1b A Word document with the draft text of the homepage.
2a-d The Norvalith logo. Two versions are included – a dark version which works well against a light background, and a light version which works well against a dark background.
3 The Norvalith color palette with HEX and RGB values. Designers are not limited to this palette, but colors should be complementary.
4 A draft of the homepage menu
5 Service sheets with information on the services we provide

MORE ABOUT NORVALITH
Norvalith is a consulting company focused on transforming businesses through software. Our tagline, “Transformation Delivered,” recognizes the gap business often have between business transformation and the software they end up with. By listening to our customers and understanding their vision and where they are, we help get our customers where they want to go.

We increase our capability by working with many consultants and partners, allowing us to provide our customers with the best people and the software that best suits them.

Industry/Entity Type

Consulting

Number of Pages Required

1 page

Font styles to use
Sans Serif

Requirements
Must have
• the content represented on the wireframe uploaded
Nice to have
• interactive features, such as roll-over icons that reveal additional information

```html
<!DOCTYPE html>
<html lang="en">
<head>
<meta charset="utf-8">
<title>Norvalith — Transformation Delivered</title>
<link href="https://fonts.googleapis.com/css2?family=Poppins:wght@300;400;500;600&display=swap" rel="stylesheet">
<style>
:root{
  --navy:#415169;
  --navy-deep:#3d4d66;
  --gold:#e3b714;
  --text:#3a4556;
  --muted:#8b93a0;
  --pill:#e6eaf0;
  --band:#eaf0f3;
  --line:#e3e7ec;
  --white:#ffffff;
}
*{box-sizing:border-box;margin:0;padding:0}
html,body{width:1200px;height:3284px;overflow:hidden}
body{position:relative;font-family:'Poppins',sans-serif;color:var(--text);background:var(--white)}
.abs{position:absolute}
a{color:inherit;text-decoration:none}

/* header */
.brand{font-size:27px;font-weight:400;color:var(--navy);letter-spacing:.5px;display:flex;align-items:center;gap:6px}
.brand-dot{width:8px;height:8px;background:var(--navy)}
.nav{top:31px;left:448px;display:flex;gap:41px;font-size:13px;color:var(--muted)}
.nav .active{color:var(--navy);font-weight:500}
.login{top:31px;left:901px;font-size:13px;color:var(--muted)}
.join{top:20px;left:955px;width:116px;height:40px;border-radius:20px;background:var(--white);box-shadow:0 2px 10px rgba(60,80,110,.08);color:var(--navy);font-size:15px;display:flex;align-items:center;justify-content:center}

/* hero */
.hero{top:0;left:0;width:1200px;height:670px;background:linear-gradient(180deg,#f4f6fa 0%,#f9fafc 60%,#eef2f6 100%);overflow:hidden}
.hero-title{top:108px;width:1200px;text-align:center;font-size:39px;font-weight:400;color:var(--navy)}
.hero-lead{top:162px;left:200px;width:800px;text-align:center;font-size:15px;line-height:25.5px;color:var(--muted);font-weight:300}
.pills{top:254px;width:1200px;display:flex;flex-direction:column;align-items:center;gap:8px}
.pill{background:var(--pill);border-radius:14px;padding:3px 18px;font-size:14px;color:#5a6577;font-weight:300}
.pill.accent{color:#3d5f9a}
.cta{top:414px;left:535px;width:130px;height:39px;border-radius:20px;background:var(--navy);color:#fff;font-size:12px;display:flex;align-items:center;justify-content:center;gap:14px;letter-spacing:.3px}
.avatar{border-radius:50%;border:4px solid #fff;box-shadow:0 3px 12px rgba(40,60,90,.18)}
.stem{width:1px;background:#cfd6df}
.pin{border-radius:50%}

/* section tech */
h2.sec{font-size:27px;font-weight:400;color:var(--navy)}
.body{font-size:15px;line-height:27px;color:var(--muted);font-weight:300}
.how{top:852px;left:893px;width:180px;height:73px;background:var(--navy);color:var(--gold);font-size:16px;line-height:22px;display:flex;align-items:center;justify-content:center;text-align:center;border-radius:2px}
.card{top:991px;width:181px;height:299px;border:1px solid var(--line);background:#fff;padding:56px 14px 0 14px}
.card.feature{background:var(--navy);border-color:var(--navy)}
.card svg.ico{width:36px;height:36px;display:block;margin-bottom:20px}
.card h3{font-size:17px;font-weight:400;line-height:22px;color:#2e3848;height:44px}
.card.feature h3{color:var(--gold);font-weight:500;font-size:18px;line-height:28px;height:56px;margin-top:-10px}
.card p{font-size:11.5px;line-height:24px;color:#4a5465;margin-top:12px;font-weight:300}
.card.feature p{color:#e4e8ee}
.arrows{position:absolute;left:14px;bottom:26px;display:flex;gap:6px}
.arr{width:21px;height:21px;display:flex;align-items:center;justify-content:center}
.arr.prev{background:var(--navy)}
.arr.next{background:transparent}
.card.feature .arr.prev{background:var(--gold)}
.card.feature .arr.next{background:#fff}

/* people */
.btn-team{top:1778px;left:125px;width:130px;height:38px;border-radius:19px;background:var(--navy);color:#fff;font-size:12px;display:flex;align-items:center;justify-content:center;gap:18px}
.photo{border-radius:50%}

/* feedback */
.band{top:2009px;left:0;width:1200px;height:539px;background:var(--band)}
.tcard{background:#fff;box-shadow:0 4px 20px rgba(60,80,110,.06);padding:25px 24px 0 122px;width:458px;height:151px}
.tcard.dim{opacity:.6}
.tcard .face{position:absolute;left:27px;top:32px;width:80px;height:88px;border-radius:50%}
.tcard p{font-size:11px;line-height:22px;color:#3c4554;font-weight:300}
.tcard .who{font-size:14px;color:var(--navy);margin-top:7px}
.tcard .role{font-size:8px;color:#555}
.quote{position:absolute;right:26px;bottom:18px}
.fb-kicker{top:2089px;left:684px;font-size:16px;color:var(--text)}
.fb-title{top:2118px;left:681px;font-size:26px;color:var(--gold);font-weight:400}
.fb-body{top:2171px;left:681px;width:405px;font-size:14.5px;line-height:27px;color:var(--text);font-weight:300}
.stat{top:2296px;left:681px;display:flex;align-items:baseline;gap:16px}
.stat b{font-size:38px;font-weight:500;color:var(--gold)}
.stat span{font-size:16px;color:#a5acb6;font-weight:500}
.more{top:2366px;left:685px;width:157px;height:52px;background:var(--navy);color:var(--gold);font-size:13.5px;font-weight:500;display:flex;align-items:center;justify-content:center;border-radius:3px}

/* partners */
.partners{top:2655px;left:125px;width:950px;display:flex;justify-content:space-between;align-items:center}
.partner{width:90px;text-align:center;font-size:17px;font-weight:600;color:#6e7277}

/* signup */
.cta-band{top:2802px;left:0;width:1200px;height:364px;background:var(--navy-deep)}
.cta-title{top:2879px;width:1200px;text-align:center;font-size:26px;color:var(--gold)}
.cta-text{top:2940px;left:270px;width:660px;text-align:center;font-size:11.5px;line-height:21.5px;color:#e7ebf0;font-weight:300}
.signup{top:3029px;left:490px;width:219px;height:60px;border-radius:30px;background:var(--gold);color:#fff;font-size:19px;font-weight:500;display:flex;align-items:center;justify-content:center}

/* footer */
.fnav{top:3218px;left:428px;display:flex;gap:20px;font-size:13px;color:var(--muted)}
.fnav .active{color:var(--navy);font-weight:500}
.copy{top:3218px;left:850px;font-size:12.5px;color:var(--muted)}
.copy b{color:var(--navy);font-weight:400}
</style>
</head>
<body>

<!-- HERO -->
<section class="abs hero">
  <svg class="abs" style="left:0;top:0" width="1200" height="670" viewBox="0 0 1200 670">
    <path d="M600 0 C700 60 620 120 760 100 L1200 0Z" fill="#eef1f6" opacity=".7"/>
    <circle cx="44" cy="348" r="11" fill="#e6eaf0"/>
    <circle cx="298" cy="341" r="6" fill="#e6eaf0"/>
    <circle cx="1124" cy="302" r="11" fill="#e6eaf0"/>
    <circle cx="1045" cy="353" r="6" fill="#e6eaf0"/>
    <path d="M0 548 C180 520 300 600 520 560 C720 520 880 590 1060 540 C1130 520 1170 530 1200 540 L1200 670 L0 670Z" fill="#eff2f6"/>
    <path d="M0 580 C220 560 380 620 600 585 C820 550 980 610 1200 575 L1200 670 L0 670Z" fill="#e7ecf1"/>
  </svg>
</section>

<div class="abs brand" style="top:22px;left:125px"><span class="brand-dot"></span>Norvalith</div>
<nav class="abs nav"><a class="active">About</a><a>Services</a><a>Insights</a><a>Contact</a></nav>
<a class="abs login">Login</a>
<a class="abs join">Join Us</a>

<h1 class="abs hero-title">Transformation Delivered.</h1>
<p class="abs hero-lead">We do more for our customers than implement software. We listen. We work to understand where they are in their transformation journey and where they want to go. We partner with them to clear the roadblocks that stand in their way, ensuring they reach their destination. At Norvalith, we:</p>
<div class="abs pills">
  <span class="pill">Focus on business value, with an emphasis on delivering value quickly.</span>
  <span class="pill accent">Meet our customers where they are without backing them up to the beginning of their journey.</span>
  <span class="pill">Provide a wide range of services, from strategy to product support.</span>
  <span class="pill">Commit to our customer’s long-term success.</span>
</div>
<a class="abs cta">GET STARTED <svg width="7" height="11" viewBox="0 0 7 11"><path d="M1 1l4.5 4.5L1 10" stroke="#fff" fill="none" stroke-width="1.3"/></svg></a>

<div class="abs stem" style="left:210px;top:432px;height:92px"></div>
<div class="abs avatar" role="img" aria-label="Portrait of a team member" style="left:180px;top:373px;width:60px;height:60px;background:linear-gradient(135deg,#f2b82a,#9a5a2a)"></div>
<div class="abs pin" style="left:204px;top:524px;width:13px;height:13px;background:#275b9a"></div>

<div class="abs stem" style="left:395px;top:470px;height:62px"></div>
<div class="abs avatar" role="img" aria-label="Portrait of a consultant" style="left:378px;top:438px;width:34px;height:34px;background:linear-gradient(135deg,#7cc6d6,#b08466)"></div>
<div class="abs pin" style="left:392px;top:534px;width:7px;height:7px;background:#c9d1db"></div>

<div class="abs stem" style="left:803px;top:470px;height:62px"></div>
<div class="abs avatar" role="img" aria-label="Portrait of a consultant" style="left:786px;top:438px;width:34px;height:34px;background:linear-gradient(135deg,#c9b9a8,#6d5548)"></div>
<div class="abs pin" style="left:800px;top:534px;width:7px;height:7px;background:#c9dbe8"></div>

<div class="abs stem" style="left:988px;top:432px;height:92px"></div>
<div class="abs avatar" role="img" aria-label="Portrait of a team member" style="left:960px;top:373px;width:60px;height:60px;background:linear-gradient(135deg,#c58ac4,#3a2a2a)"></div>
<div class="abs pin" style="left:983px;top:524px;width:13px;height:13px;background:var(--gold)"></div>

<!-- TECHNOLOGY -->
<h2 class="abs sec" style="top:808px;left:125px">Transformation Supported by Technology</h2>
<p class="abs body" style="top:852px;left:125px;width:735px">During our early years, Norvalith focused only on business transformation. We came to realize that successful transformation often depended on quality software implementations, and often more than one. Now we focus on five things, the five things most businesses need to reach their goals.</p>
<a class="abs how">How We<br>Work Button</a>

<article class="abs card feature" style="left:125px">
  <svg class="ico" viewBox="0 0 36 36"><rect x="10" y="3" width="22" height="20" rx="3" fill="none" stroke="#e3b714" stroke-width="1.3"/><rect x="3" y="11" width="22" height="20" rx="3" fill="#415169" stroke="#e3b714" stroke-width="1.3"/><path d="M9 21l3.5 3.5L19 17" stroke="#e3b714" fill="none" stroke-width="1.3"/></svg>
  <h3>Business Transformation</h3>
  <p>Define and execute your strategy.</p>
  <div class="arrows"><span class="arr prev"><svg width="7" height="11"><path d="M6 1L1.5 5.5 6 10" stroke="#fff" fill="none" stroke-width="1.4"/></svg></span><span class="arr next"><svg width="7" height="11"><path d="M1 1l4.5 4.5L1 10" stroke="#415169" fill="none" stroke-width="1.4"/></svg></span></div>
</article>

<article class="abs card" style="left:316px">
  <svg class="ico" viewBox="0 0 36 36"><rect x="4" y="5" width="28" height="19" fill="none" stroke="#8a94a3" stroke-width="1.2"/><path d="M9 19l6-6 4 4 7-7" stroke="#8a94a3" fill="none" stroke-width="1.2"/><path d="M18 24v6M13 31h10" stroke="#8a94a3" stroke-width="1.2"/></svg>
  <h3>ERP<br>Implementations</h3>
  <p>Assess, upgrade, and implement ERP solutions to meet your needs.</p>
  <div class="arrows"><span class="arr prev"><svg width="7" height="11"><path d="M6 1L1.5 5.5 6 10" stroke="#fff" fill="none" stroke-width="1.4"/></svg></span><span class="arr next"><svg width="7" height="11"><path d="M1 1l4.5 4.5L1 10" stroke="#415169" fill="none" stroke-width="1.4"/></svg></span></div>
</article>

<article class="abs card" style="left:508px">
  <svg class="ico" viewBox="0 0 36 36"><rect x="4" y="4" width="28" height="28" rx="7" fill="none" stroke="#8a94a3" stroke-width="1.2"/><rect x="10" y="10" width="16" height="14" fill="none" stroke="#8a94a3" stroke-width="1.2"/><path d="M13 15h10M13 19h10" stroke="#8a94a3" stroke-width="1.2"/></svg>
  <h3>CRM<br>Implementations</h3>
  <p>Take your relationships to the next level.</p>
  <div class="arrows"><span class="arr prev"><svg width="7" height="11"><path d="M6 1L1.5 5.5 6 10" stroke="#fff" fill="none" stroke-width="1.4"/></svg></span><span class="arr next"><svg width="7" height="11"><path d="M1 1l4.5 4.5L1 10" stroke="#415169" fill="none" stroke-width="1.4"/></svg></span></div>
</article>

<article class="abs card" style="left:700px">
  <svg class="ico" viewBox="0 0 36 36"><rect x="3" y="5" width="24" height="17" rx="2" fill="none" stroke="#8a94a3" stroke-width="1.2"/><rect x="18" y="13" width="15" height="19" rx="2" fill="#fff" stroke="#8a94a3" stroke-width="1.2"/><path d="M8 27h10" stroke="#8a94a3" stroke-width="1.2"/></svg>
  <h3>BI<br>and Data</h3>
  <p>Discover, connect, and trust your data.</p>
  <div class="arrows"><span class="arr prev"><svg width="7" height="11"><path d="M6 1L1.5 5.5 6 10" stroke="#fff" fill="none" stroke-width="1.4"/></svg></span><span class="arr next"><svg width="7" height="11"><path d="M1 1l4.5 4.5L1 10" stroke="#415169" fill="none" stroke-width="1.4"/></svg></span></div>
</article>

<article class="abs card" style="left:892px">
  <svg class="ico" viewBox="0 0 36 36"><circle cx="13" cy="11" r="6" fill="none" stroke="#8a94a3" stroke-width="1.2"/><path d="M3 31c0-7 5-11 10-11s10 4 10 11" fill="none" stroke="#8a94a3" stroke-width="1.2"/><path d="M23 8a5 5 0 010 9M27 22c4 1 6 4 6 8" fill="none" stroke="#8a94a3" stroke-width="1.2"/></svg>
  <h3>Building the Right Team of People</h3>
  <p>Hire resources for your transformation journey.</p>
  <div class="arrows"><span class="arr prev"><svg width="7" height="11"><path d="M6 1L1.5 5.5 6 10" stroke="#fff" fill="none" stroke-width="1.4"/></svg></span><span class="arr next"><svg width="7" height="11"><path d="M1 1l4.5 4.5L1 10" stroke="#415169" fill="none" stroke-width="1.4"/></svg></span></div>
</article>

<p class="abs body" style="top:1317px;left:125px">Find out how Norvalith can help you put all the pieces together and get them done.</p>

<!-- PEOPLE -->
<h2 class="abs sec" style="top:1465px;left:125px">It’s the People</h2>
<p class="abs body" style="top:1509px;left:125px;width:630px">The world has changed in the past twenty years. The people you need might not all work for one company. Our clients want the best resources, available quickly. That’s why, in addition to our team of experts, we partner with:</p>
<p class="abs body" style="top:1605px;left:125px;width:630px">• A large network of expert consultants who are the best at what they do,<br>• Service providers all over the world to provide the resources and value<br>that are right for you, <span style="color:var(--navy)">available 24 x 7.</span></p>
<p class="abs body" style="top:1706px;left:125px;width:660px">People are invariably at the center of our customer’s success. Find out how we can add our experts to yours.</p>
<a class="abs btn-team">OUR TEAM <svg width="7" height="11"><path d="M1 1l4.5 4.5L1 10" stroke="#fff" fill="none" stroke-width="1.2"/></svg></a>

<div class="abs photo" role="img" aria-label="Photo of a young woman consultant" style="left:756px;top:1531px;width:116px;height:116px;background:radial-gradient(circle at 50% 40%,#b98a76,#5b4a48 70%)"></div>
<div class="abs photo" role="img" aria-label="Photo of a senior male consultant" style="left:885px;top:1477px;width:148px;height:148px;background:radial-gradient(circle at 50% 40%,#8a5e46,#e9e5df 72%)"></div>
<div class="abs photo" role="img" aria-label="Photo of a young man on a yellow background" style="left:823px;top:1644px;width:104px;height:104px;background:radial-gradient(circle at 50% 50%,#3b332c,#d4a623 75%)"></div>
<div class="abs photo" role="img" aria-label="Photo of a smiling woman outdoors" style="left:949px;top:1629px;width:124px;height:124px;background:radial-gradient(circle at 50% 40%,#d6b79a,#6b8aa0 72%)"></div>

<!-- FEEDBACK -->
<section class="abs band"></section>

<div class="abs tcard dim" style="left:65px;top:1955px">
  <div class="face" role="img" aria-label="Client portrait" style="background:linear-gradient(135deg,#d9cdbf,#8d7d70)"></div>
  <p>Lorem ipsum is simply dummy text of the printing and typesetting industry. Lorem Ipsum has been the industry's standard dummy text ever since the 1500s,</p>
  <div class="who">Daniel Hartwell</div><div class="role">CEO</div>
  <svg class="quote" width="27" height="22"><path d="M0 0h11v22l-5-5H0zM15 0h11v22l-5-5h-6z" fill="#415169"/></svg>
</div>

<div class="abs tcard" style="left:125px;top:2139px">
  <div class="face" role="img" aria-label="Client portrait" style="background:linear-gradient(135deg,#3a6a86,#5b4034)"></div>
  <p>Lorem Ipsum is simply dummy text of the printing and typesetting industry. Lorem Ipsum has been the industry's standard dummy text ever since the 1500s,</p>
  <div class="who" style="margin-top:4px">Daniel Hartwell</div><div class="role">CEO</div>
  <svg class="quote" width="27" height="22"><path d="M0 0h11v22l-5-5H0zM15 0h11v22l-5-5h-6z" fill="#415169"/></svg>
</div>

<div class="abs tcard dim" style="left:65px;top:2320px">
  <div class="face" role="img" aria-label="Client portrait" style="background:linear-gradient(135deg,#777,#3e3e3e)"></div>
  <p>Lorem ipsum is simply dummy text of the printing and typesetting industry. Lorem Ipsum has been the industry's standard dummy text ever since the 1500s,</p>
  <div class="who">Daniel Hartwell</div><div class="role">CEO</div>
  <svg class="quote" width="27" height="22"><path d="M0 0h11v22l-5-5H0zM15 0h11v22l-5-5h-6z" fill="#415169"/></svg>
</div>

<div class="abs fb-kicker">Clients Feedback</div>
<h2 class="abs fb-title">Clients Feedback</h2>
<p class="abs fb-body">“Lorem Ipsum is simply dummy text of the printing and typesetting industry. Lorem Ipsum has been the industry's standard dummy text ever since the 1500s, Lorem Ipsum is simply dummy text of the printing</p>
<div class="abs stat"><b>450+</b><span>clients feeback</span></div>
<a class="abs more">See More Reviews</a>

<!-- PARTNERS -->
<div class="abs partners">
  <span class="partner">Arvedo</span>
  <span class="partner">Coravel</span>
  <span class="partner">Kestro</span>
  <span class="partner">Pilgra</span>
  <span class="partner">Wendmar</span>
  <span class="partner">Bravolo</span>
</div>

<!-- SIGN UP -->
<section class="abs cta-band"></section>
<h2 class="abs cta-title" style="font-weight:400">It’s Time To Change Your Life Today</h2>
<p class="abs cta-text">Lorem Ipsum is simply dummy text of the printing and typesetting Lorem Ipsum is simply dummy text of the printing and typesetting&nbsp; Lorem Ipsum is simply dummy text of the printing and typesetting Lorem Ipsum is simply dummy text of the printing and typesetting</p>
<a class="abs signup">Sign Up</a>

<!-- FOOTER -->
<div class="abs brand" style="top:3206px;left:125px;font-size:36px;color:#8a9bb5"><span class="brand-dot" style="background:#8a9bb5"></span>Norvalith</div>
<nav class="abs fnav"><a class="active">Home</a><a>About Us</a><a>Services</a><a>Insights</a><a>Contact Us</a></nav>
<p class="abs copy"><b>2023 Norvalith</b> . All Rights Reserved.</p>

</body>
</html>
```